Young Accounting firm needing a captivating business card

We need a business card design that forces the person to look at the card because its either gold foil, plastic, or lettering pop up etc. We already have a logo with a specific gold color and we need to make it pop. We are an accounting firm. I need the words" accounting, payroll, licenses, audits, taxes" somewhere on the business card so as to describe what we do- preferably on the side where the logo is at.

Industry/Entity Type

Accounting

Contact Information for Business Card

Address 48276 9th Ave S Ste 305, Federal Way, WA 98117
Business Phone (360)418-2096
Fax (360)418-2157
Office Cell Phone (360)586-7319

Font styles to use
Serif

Colors
85abd2

Requirements
Must have
• It should state
• "Accounting" "Taxes" "Audits" "Licenses" "Payroll"
Nice to have
• Matte with gold foil, different textures, With Either a textured ivory background or gray blue slate background
Should not have
• colorful colors

```html
<!DOCTYPE html>
<html lang="en">
<head>
<meta charset="utf-8">
<title>Kelmont Tax – Business Card</title>
<link href="https://fonts.googleapis.com/css2?family=EB+Garamond:wght@400;500&display=swap" rel="stylesheet">
<style>
  :root {
    --backdrop: #e9e7e3;
    --card-blue: #85abd2;
    --gold: #d2a645;
    --text-light: #ffffff;
    --shadow: rgba(40, 50, 60, 0.22);
  }
  * { margin: 0; padding: 0; box-sizing: border-box; }
  html, body {
    width: 1200px; height: 862px; overflow: hidden;
    background: var(--backdrop);
    font-family: "EB Garamond", Georgia, serif;
  }
  .stage { position: relative; width: 1200px; height: 862px; }
  .card {
    position: absolute;
    width: 560px; height: 320px;
    background: var(--card-blue);
    box-shadow: 0 10px 26px var(--shadow);
  }
  .card--front { left: 80px; top: 90px; }
  .card--back  { left: 560px; top: 452px; }

  .brand { display: flex; align-items: center; gap: 12px; color: var(--gold); font-weight: 500; }
  .brand__mark { width: 30px; height: 30px; background: var(--gold); }
  .card--front .brand {
    position: absolute; left: 0; right: 0; top: 110px; justify-content: center;
    font-size: 46px; letter-spacing: 0.5px;
  }
  .services {
    position: absolute; left: 0; right: 0; bottom: 44px;
    text-align: center; color: var(--text-light); font-size: 17px; letter-spacing: 0.3px;
  }
  .services .divider { color: var(--gold); margin: 0 8px; }

  .card--back .brand {
    position: absolute; left: 36px; top: 136px; font-size: 36px; gap: 10px;
  }
  .card--back .brand__mark { width: 24px; height: 24px; }
  .rule {
    position: absolute; left: 290px; top: 64px; width: 1px; height: 196px; background: var(--gold);
  }
  .contact { position: absolute; left: 310px; top: 60px; color: var(--text-light); font-size: 15px; line-height: 1.35; }
  .contact__name { color: var(--gold); font-size: 23px; letter-spacing: 1px; font-weight: 500; line-height: 1.1; }
  .contact__title { font-size: 14px; margin-bottom: 12px; }
  .contact__address { margin-bottom: 10px; }
  .contact__list { list-style: none; }
  .contact__list li { display: flex; align-items: center; gap: 10px; }
  .contact__list svg { width: 12px; height: 12px; fill: var(--gold); flex: none; }
</style>
</head>
<body>
<main class="stage">
  <section class="card card--front" aria-label="Business card front">
    <div class="brand"><span class="brand__mark"></span><span>Kelmont Tax</span></div>
    <p class="services">Accounting<span class="divider">|</span>Taxes<span class="divider">|</span>Audits<span class="divider">|</span>Licenses<span class="divider">|</span>Payroll</p>
  </section>

  <section class="card card--back" aria-label="Business card back">
    <div class="brand"><span class="brand__mark"></span><span>Kelmont Tax</span></div>
    <div class="rule"></div>
    <div class="contact">
      <p class="contact__name">MARCUS HALE</p>
      <p class="contact__title">Owner</p>
      <p class="contact__address">48276 9th Ave S Ste 305,<br>Federal Way, WA 98117</p>
      <ul class="contact__list">
        <li><svg viewBox="0 0 12 12"><path d="M2.5 0.5l2 2.5-1.2 1.4c0.8 1.6 2.1 2.9 3.8 3.8l1.4-1.2 2.5 2-1.3 2.3C5.2 11 1 6.8 0.2 1.8z"/></svg>(360)418-2096</li>
        <li><svg viewBox="0 0 12 12"><path d="M3 0h6v12H3zM4 1.5v8h4v-8z"/></svg>(360)586-7319</li>
        <li><svg viewBox="0 0 12 12"><path d="M3 0h6v3H3zM0 4h12v6h-2v2H2v-2H0zM3 8v3h6V8z"/></svg>(360)418-2157</li>
        <li><svg viewBox="0 0 12 12"><path d="M0 2h12v8H0zM1 3l5 4 5-4v-0.2H1z" fill-rule="evenodd"/></svg>info@marcushale.com</li>
      </ul>
    </div>
  </section>
</main>
</body>
</html>
```